Business Card Design Project For Moving Company

Hello,

We need the business card to be 2 sided and we were thinking to use the logo on the front of the card (see file 1 attached) and the text "logo" (see file 2 attached) in the back of the card. We're looking for a powerful design that will help us build our brand, as our company is new.
We are a full service moving company (no storage) located in San Diego, CA, USA. The design should communicate to our potential customers that we have the highest level of service, customer satisfaction is our number one goal, our team is professional and efficient.

Thank you,

Dorn
Updates

Project Deadline Extended
Reason: We would like to have more time to provide feedback for the designs already submitted. Thank you, Dorn

Industry/Entity Type

Moving Company

Requirements
Must have
• Front of the card must have the following text and logo:
Haulbright, Inc
Residential And Commercial
Local And Long Distance
Address: 7312 Quillmont Rd, #146,
San Diego, CA, 92784
P: 855-372-LIFT (5438)
F: 858-529-4407
info@haul-bright.com
www.haul-bright.com

Back of the card must have the following text and text "logo" (file 2 attached):

The best compliment we can ever receive is a referral from our clients.

```html
<!DOCTYPE html>
<html lang="en">
<head>
<meta charset="utf-8">
<title>Haulbright, Inc — Business Card</title>
<link rel="stylesheet" href="https://fonts.googleapis.com/css2?family=Oswald:wght@400;500;700&family=Open+Sans:wght@400;600&display=swap">
<style>
  :root {
    --stage: #3a3a3a;
    --paper: #ffffff;
    --ink-dark: #2a2a2e;
    --ink-grey: #8a8a8a;
    --brand-red: #d7001b;
    --band-top: #2a1418;
    --band-mid: #7a0a18;
    --rule: rgba(255,255,255,0.85);
    --text-light: #ffffff;
  }
  * { box-sizing: border-box; margin: 0; padding: 0; }
  html, body {
    width: 1200px; height: 900px; overflow: hidden;
    background: var(--stage);
  }
  .canvas { position: relative; width: 1200px; height: 900px; }

  .card {
    position: absolute;
    background: var(--paper);
    box-shadow: 0 2px 6px rgba(0,0,0,0.35);
    overflow: hidden;
  }

  /* Back of card (horizontal) */
  .card-back { left: 181px; top: 301px; width: 514px; height: 296px; }
  .card-back .wordmark {
    position: absolute; left: 0; right: 0; top: 118px;
    text-align: center;
    font-family: 'Oswald', sans-serif; font-weight: 700;
    font-size: 54px; line-height: 1; letter-spacing: 0.5px;
    color: var(--ink-dark);
  }
  .card-back .tagline {
    position: absolute; left: 0; right: 0; top: 208px;
    text-align: center;
    font-family: 'Oswald', sans-serif; font-weight: 500;
    font-size: 11.5px; letter-spacing: 0.2px;
    text-transform: uppercase; color: var(--ink-grey);
  }

  /* Front of card (vertical) */
  .card-front { left: 723px; top: 193px; width: 297px; height: 514px; }
  .card-front .brand-area {
    position: absolute; left: 0; right: 0; top: 0; height: 232px;
    display: flex; align-items: center; justify-content: center; gap: 10px;
  }
  .brand-area .brand-square { width: 22px; height: 22px; background: var(--brand-red); }
  .brand-area .brand-name {
    font-family: 'Oswald', sans-serif; font-weight: 700;
    font-size: 34px; color: var(--ink-dark); line-height: 1;
  }
  .card-front .band {
    position: absolute; left: 0; top: 224px; width: 297px; height: 290px;
  }
  .card-front .details {
    position: absolute; left: 0; right: 0; top: 270px;
    text-align: center; color: var(--text-light);
    font-family: 'Open Sans', sans-serif;
  }
  .details .company {
    font-family: 'Oswald', sans-serif; font-weight: 700;
    font-size: 23px; line-height: 1.1;
  }
  .details .services { font-size: 13px; line-height: 17px; margin-top: 4px; }
  .details .rule {
    width: 204px; height: 1px; background: var(--rule); margin: 8px auto 9px;
  }
  .details .label { font-size: 8.5px; line-height: 10px; }
  .details .value { font-size: 13px; line-height: 16px; }
  .details .web { font-size: 13px; line-height: 17px; }
</style>
</head>
<body>
<main class="canvas">

  <section class="card card-back" aria-label="Back of business card">
    <div class="wordmark">HAULBRIGHT</div>
    <p class="tagline">The best compliment we can ever receive is a referral from our clients</p>
  </section>

  <section class="card card-front" aria-label="Front of business card">
    <div class="brand-area">
      <span class="brand-square"></span>
      <span class="brand-name">Haulbright</span>
    </div>

    <svg class="band" viewBox="0 0 297 290" preserveAspectRatio="none" aria-hidden="true">
      <defs>
        <linearGradient id="bandFill" x1="0" y1="0" x2="0" y2="1">
          <stop offset="0" stop-color="var(--band-top)"/>
          <stop offset="0.5" stop-color="var(--band-mid)"/>
          <stop offset="1" stop-color="var(--brand-red)"/>
        </linearGradient>
      </defs>
      <path d="M0 12 Q148 -2 297 12 L297 290 L0 290 Z" fill="#d6d6d6"/>
      <path d="M0 18 Q148 4 297 18 L297 290 L0 290 Z" fill="url(#bandFill)"/>
    </svg>

    <div class="details">
      <div class="company">Haulbright, Inc</div>
      <div class="services">Residential And Commercial<br>Local And Long Distance</div>
      <div class="rule"></div>
      <div class="label">Adress</div>
      <div class="value">7312 Quillmont Rd, #146,<br>San Diego, CA, 92784</div>
      <div class="label">Phone</div>
      <div class="value">855-372-LIFT (5438)</div>
      <div class="label">Fax</div>
      <div class="value">858-529-4407</div>
      <div class="rule"></div>
      <div class="web">info@haul-bright.com<br>www.haul-bright.com</div>
    </div>
  </section>

</main>
</body>
</html>
```